Amber Reed Properties, which offers a selection of prime properties (villas

A website that contains: Idea, benefits, destinations (villas), offers, about us, contact, newsletter, social media, blog, look at the attachment, even if it is in German. The idea is that I can easily add new pages, if necessary, with the design you make. Later on we want to add a reservation system, so you can book your villa through the internet. Besides, there is a concierge service available, which organizes everything for the customer, owner, from villa to restaurant, limo service, ... & benefits and emotions through nice pictures / videos, they should be convinced to invest.

Target Market(s)

Investors (golfer and non-golfer) which have 300'000 to invest in a kind of real-estate investing club

Number of Pages Required

5+ page

Font styles to use
Sans Serif

Requirements
Must have
• It must be for wordpress, must have an exclusive touch, high quality, with nice pictures of golf courses. The Logo is gold so it has to match with gold, the font is segan or segoe semilight or similar, sans serif
Nice to have
• may be as well as the possibility to include videos of the different destinations and houses

```html
<!DOCTYPE html>
<html lang="de">
<head>
<meta charset="utf-8">
<title>Amber Reed Properties – Ihr Nutzen</title>
<link href="https://fonts.googleapis.com/css2?family=Oswald:wght@300;400&family=Open+Sans:wght@300&display=swap" rel="stylesheet">
<style>
  :root {
    --bg: #171717;
    --bg-top: #1b1b1b;
    --gold: #d4a22c;
    --text: #d6d6d6;
    --text-soft: #cfcfcf;
    --rule: #8a8a8a;
  }
  * { margin: 0; padding: 0; box-sizing: border-box; }
  html, body { width: 1200px; height: 1200px; overflow: hidden; }
  body {
    background: var(--bg);
    font-family: "Open Sans", sans-serif;
    font-weight: 300;
    color: var(--text);
    position: relative;
  }
  .top-bar {
    position: absolute; left: 0; top: 0; width: 1200px; height: 28px;
    background: var(--bg-top);
    border-bottom: 1px solid #232323;
  }
  .section-title {
    position: absolute; left: 0; width: 1200px;
    text-align: center;
  }
  .ornament {
    display: block; margin: 0 auto;
  }
  .kicker {
    font-family: "Oswald", sans-serif; font-weight: 400;
    font-size: 15px; color: #f0f0f0; letter-spacing: 0.5px;
    line-height: 1; margin-top: 8px;
  }
  .heading {
    font-family: "Oswald", sans-serif; font-weight: 300;
    color: var(--gold); font-size: 40px; line-height: 1;
    letter-spacing: 1px; margin: 2px 0 6px;
  }
  .benefits-photo {
    position: absolute; left: 129px; top: 164px; width: 351px; height: 302px;
    border-radius: 5px;
    background: linear-gradient(180deg, #8fa7c4 0%, #b9c6d3 30%, #6e7f86 42%, #5d7d3e 55%, #4e7a2a 75%, #8a6e55 100%);
  }
  .benefit-list {
    position: absolute; left: 531px; top: 168px; width: 545px;
    list-style: none; font-size: 17.5px; line-height: 21.5px;
  }
  .benefit-list li { margin-bottom: 13px; }
  .club-band {
    position: absolute; left: 0; top: 507px; width: 1200px; height: 480px;
    background:
      radial-gradient(ellipse at 40% 85%, rgba(70,90,50,0.55), transparent 60%),
      linear-gradient(180deg, #2a2826 0%, #302d2a 45%, #33382a 75%, #2f3529 100%);
  }
  .club-text {
    position: absolute; left: 100px; top: 634px; width: 1000px;
    text-align: center; font-size: 17.5px; line-height: 21.5px; color: var(--text-soft);
  }
  .club-text p { margin-bottom: 13px; }
  .club-text p.tall { line-height: 25px; }
  .options-heading { font-size: 40px; letter-spacing: 1.5px; }
  .option-row {
    position: absolute; left: 130px; top: 1164px; width: 938px; height: 36px;
    background: #101010;
  }
  .option-card {
    position: absolute; top: 1173px; height: 27px; background: #151515;
    font-family: "Oswald", sans-serif; font-weight: 300;
    color: var(--gold); font-size: 23px; line-height: 1;
    padding-top: 6px; letter-spacing: 0.5px;
  }
  .card-albatros { left: 130px; width: 294px; padding-left: 20px; }
  .card-eagle { left: 430px; width: 310px; padding-left: 25px; }
  .card-birdie { left: 744px; width: 324px; padding-left: 48px; }
</style>
</head>
<body>
  <div class="top-bar"></div>

  <header class="section-title" style="top:48px;">
    <svg class="ornament" width="108" height="10" viewBox="0 0 108 10">
      <line x1="0" y1="1" x2="108" y2="1" stroke="var(--rule)" stroke-width="1"/>
      <line x1="6" y1="5" x2="102" y2="5" stroke="var(--rule)" stroke-width="1"/>
      <line x1="12" y1="9" x2="96" y2="9" stroke="var(--rule)" stroke-width="1"/>
    </svg>
    <div class="kicker">IHR NUTZEN</div>
    <h2 class="heading">MONETAR</h2>
    <svg class="ornament" width="108" height="10" viewBox="0 0 108 10">
      <line x1="12" y1="1" x2="96" y2="1" stroke="var(--rule)" stroke-width="1"/>
      <line x1="6" y1="5" x2="102" y2="5" stroke="var(--rule)" stroke-width="1"/>
      <line x1="0" y1="9" x2="108" y2="9" stroke="var(--rule)" stroke-width="1"/>
    </svg>
  </header>

  <div class="benefits-photo" role="img" aria-label="Terrasse mit Loungesessel und Whirlpool vor Golfplatz, Palmen und Bergkulisse"></div>

  <ul class="benefit-list">
    <li>Sie werden mit einer verhältnismässig geringen Investition Miteigentümer mehrerer, exklusiver Immobilien</li>
    <li>Sie teilen die Kauf- und Verwaltungsgebühren mit anderen Eigentümern</li>
    <li>Sie sparen bei Ihren Ferien mindestens 1/3 des marktüblichen Mietpreises für gleichwertige Traumimmobilien.</li>
    <li>Sie profitieren von einer Wertsteigerung des Portfolios</li>
    <li>Sie profitieren über den Fonds von den Mieteinnahmen des Immobil-ien-Portfolios</li>
  </ul>

  <section class="club-band" role="img" aria-label="Abgedunkeltes Foto einer Villa mit Rasenfläche"></section>

  <header class="section-title" style="top:532px;">
    <svg class="ornament" width="108" height="10" viewBox="0 0 108 10">
      <line x1="0" y1="1" x2="108" y2="1" stroke="var(--rule)" stroke-width="1"/>
      <line x1="6" y1="5" x2="102" y2="5" stroke="var(--rule)" stroke-width="1"/>
      <line x1="0" y1="9" x2="108" y2="9" stroke="var(--rule)" stroke-width="1"/>
    </svg>
    <h2 class="heading" style="margin:10px 0 10px;">MONETAR</h2>
    <svg class="ornament" width="108" height="10" viewBox="0 0 108 10">
      <line x1="0" y1="1" x2="108" y2="1" stroke="var(--rule)" stroke-width="1"/>
      <line x1="6" y1="5" x2="102" y2="5" stroke="var(--rule)" stroke-width="1"/>
      <line x1="0" y1="9" x2="108" y2="9" stroke="var(--rule)" stroke-width="1"/>
    </svg>
  </header>

  <div class="club-text">
    <p class="tall">Als Investor werden Sie Mitglied im Amber Reed Owners Club, welcher mittels des Concierge<br>Services die Nutzung regelt und organisiert</p>
    <p>Auf eine Immobilie kommen nur 4 Investoren – damit ist eine gute Verfügbarkeit gewährleistet</p>
    <p>Mit einer geplanten Nutzung von je 4 Wochen, wird eine Belegung von 16 Wochen erzielt. Somit bleiben max. 36 Wochen<br>für Zusatzwochen der Mitglieder und die Vermietung im freien Markt</p>
    <p>Jede Immobilie hat einen Immobilien(Grösse)- und einen Monatsfaktor (Saisonalität), welche multipliziert miteinander die<br>notwendige Anzahl Golfbälle für die Nutzung ergeben. Die Golfbälle haben einen Wert von CHF 150.-.</p>
    <p>Gemäss Investment, erhält der Investor jedes Jahr ein Golfballguthaben für die Nutzung der Immobilien</p>
    <p class="tall">Er kann jedoch sein Guthaben auch ins nächste Jahr nehmen, seinen Freunden übertragen<br>oder dem Club Management anbieten</p>
    <p>Der Miteigentümer kann (falls verfügbar) auch Zusatzwochen kaufen</p>
  </div>

  <header class="section-title" style="top:1037px;">
    <svg class="ornament" width="108" height="10" viewBox="0 0 108 10">
      <line x1="0" y1="1" x2="108" y2="1" stroke="var(--rule)" stroke-width="1"/>
      <line x1="6" y1="5" x2="102" y2="5" stroke="var(--rule)" stroke-width="1"/>
      <line x1="0" y1="9" x2="108" y2="9" stroke="var(--rule)" stroke-width="1"/>
    </svg>
    <h2 class="heading options-heading" style="margin:13px 0 11px;">INVESTMENTOPTIONEN FÜR PRIVATPERSONEN UND FIRMEN</h2>
    <svg class="ornament" width="108" height="10" viewBox="0 0 108 10">
      <line x1="0" y1="1" x2="108" y2="1" stroke="var(--rule)" stroke-width="1"/>
      <line x1="6" y1="5" x2="102" y2="5" stroke="var(--rule)" stroke-width="1"/>
      <line x1="0" y1="9" x2="108" y2="9" stroke="var(--rule)" stroke-width="1"/>
    </svg>
  </header>

  <div class="option-row"></div>
  <div class="option-card card-albatros">OWNERSHIP ALBATROS:</div>
  <div class="option-card card-eagle">OWNERSHIP EAGLE:</div>
  <div class="option-card card-birdie">OWNERSHIP BIRDIE:</div>
</body>
</html>
```